Billboard design for a small town Oral Surgeon

We are getting several billboards and need a design that highlights the doctors photo, and bullet points of what he does. Our business name is extremely long, so it’s a challenge to figure out how to do this. Maybe just use our logo? Open to ideas.
The logo can be shortened as designer sees fit, meaning we can drop the tag line. Important info to include:
Doctors name is Lorvik Tamsen
The highlighted bullet points are:
•Implants
•wisdom teeth
•Jaw Surgery
•facial trauma
The goal of this billboard is to let our community know that they have an option here in Ada, our town. Many still drive to the city a couple hours away not knowing they now have an option here at home. Having a hard time finding examples of what I have in mind, so hoping this will get us going. I want it as “non-busy” as possible, so no unnecessary lines or anything that competes with the information we are trying to get across.

Target Market(s)

Everyone in town, just trying to spread the word that we are here

Industry/Entity Type

Medical/surgical (oral surgery)

Font styles to use
Sans Serif

Colors
0094D4
00A9DD
6FCCEA
C7EBF8
E9F6FB

Requirements
Must have
• *New note** Due to location of billboard, I prefer the photo of doctor to be on the left side. Must look neat and professional. Must highlight what we do.
Nice to have
• Our colors are a blue-green with silver, against black or white, but I’m flexible on this, I don’t necessarily need the colors highlighted. I’m also flexible on font style, just needs to be easy to read.
Should not have
• Distracting graphics, should not look like a dental office. That’s an issue we have is people thinking we are another dental office, we do not do any general dentistry, it’s surgery only.

```html
<!DOCTYPE html>
<html lang="en">
<head>
<meta charset="utf-8">
<title>Oral Surgeon Billboard</title>
<link rel="stylesheet" href="https://fonts.googleapis.com/css2?family=Oswald:wght@500;600&family=Montserrat:wght@600;700&display=swap">
<style>
  :root{
    --page:#e4e5e6;
    --ink:#3a3d40;
    --teal:#0a93b8;
    --green:#13a38c;
    --orange:#e8760c;
    --label:#4b4f54;
    --white:#ffffff;
  }
  *{margin:0;padding:0;box-sizing:border-box}
  html,body{width:1109px;height:1200px;overflow:hidden;background:var(--page)}
  .billboard{
    position:absolute;left:30px;top:425px;width:1049px;height:349px;
    background:linear-gradient(120deg,#ffffff 0%,#f1f2f3 55%,#ffffff 100%);
    box-shadow:0 18px 30px rgba(0,0,0,.18);
    overflow:hidden;
  }
  .billboard__art{position:absolute;inset:0}
  .doctor-name{
    position:absolute;left:36px;top:252px;white-space:nowrap;
    font:500 17px/1 "Oswald",sans-serif;color:var(--white);
    transform:scaleY(1.15);transform-origin:left top;
  }
  .tagline{
    position:absolute;left:358px;top:24px;white-space:nowrap;
    font:500 19px/1 "Oswald",sans-serif;color:var(--ink);
    transform:scaleY(1.15);transform-origin:left top;
  }
  .tagline em{font-style:normal;color:var(--teal)}
  .headline{
    position:absolute;left:356px;top:52px;white-space:nowrap;
    font:600 54px/1 "Oswald",sans-serif;color:var(--teal);letter-spacing:-.3px;
    transform:scaleY(1.15);transform-origin:left top;
  }
  .brand{
    position:absolute;left:892px;top:22px;width:110px;text-align:center;
    font:600 15px/1.15 "Oswald",sans-serif;color:var(--teal);letter-spacing:.5px;
  }
  .brand__dot{display:block;width:46px;height:46px;margin:4px auto 10px;border-radius:50%;border:5px solid var(--teal)}
  .services{position:absolute;left:360px;top:144px;display:flex;gap:10px;list-style:none}
  .service{width:151px;text-align:center}
  .service__photo{display:block;height:99px;border:2px solid var(--green);border-radius:8px}
  .service__label{margin-top:10px;font:700 15px/1 "Montserrat",sans-serif;color:var(--label)}
  .call{
    position:absolute;left:36px;top:292px;height:50px;display:flex;align-items:center;gap:14px;color:var(--white);
  }
  .call__lead{font:500 32px/1 "Oswald",sans-serif;transform:scaleY(1.12)}
  .call__number{font:700 42px/1 "Montserrat",sans-serif;letter-spacing:-.5px;display:flex;align-items:center;gap:6px}
  .address{
    position:absolute;left:558px;top:304px;display:flex;align-items:center;gap:9px;white-space:nowrap;
    font:700 20px/1 "Montserrat",sans-serif;color:var(--white);
  }
</style>
</head>
<body>
<section class="billboard">
  <svg class="billboard__art" width="1049" height="349" viewBox="0 0 1049 349" aria-hidden="true">
    <defs>
      <radialGradient id="portraitTone" cx="45%" cy="40%" r="70%">
        <stop offset="0" stop-color="#6b5a50"/>
        <stop offset=".45" stop-color="#3a3a3d"/>
        <stop offset="1" stop-color="#1c1e21"/>
      </radialGradient>
      <linearGradient id="blueArc" x1="0" y1="0" x2="0" y2="1">
        <stop offset="0" stop-color="#0094D4"/><stop offset=".6" stop-color="#00A9DD"/><stop offset="1" stop-color="#6FCCEA"/>
      </linearGradient>
      <linearGradient id="silverArc" x1="0" y1="0" x2="0" y2="1">
        <stop offset="0" stop-color="#e9eaeb"/><stop offset=".5" stop-color="#9ea2a6"/><stop offset="1" stop-color="#d6d8da"/>
      </linearGradient>
      <linearGradient id="callBar" x1="0" y1="0" x2="1" y2="0">
        <stop offset="0" stop-color="#13a38c"/><stop offset="1" stop-color="#1cc7ae"/>
      </linearGradient>
      <linearGradient id="addrBar" x1="0" y1="0" x2="1" y2="0">
        <stop offset="0" stop-color="#7d8287"/><stop offset="1" stop-color="#a6aaae"/>
      </linearGradient>
    </defs>
    <path d="M262 0 H282 C345 80 338 210 262 286 H236 C312 210 322 80 262 0 Z" fill="url(#silverArc)"/>
    <path d="M222 0 H258 C318 70 318 200 250 286 H226 C292 200 294 70 222 0 Z" fill="url(#blueArc)"/>
    <path d="M0 0 H210 C262 60 272 180 236 247 H0 Z" fill="url(#portraitTone)" role="img" aria-label="Portrait of Dr. Lorvik Tamsen in a dark suit and red tie"/>
    <path d="M338 84 C300 68 260 78 234 100" fill="none" stroke="#b5b9bd" stroke-width="5" stroke-linecap="round"/>
    <path d="M214 114 L226 88 L244 106 Z" fill="#b5b9bd"/>
    <path d="M0 247 H262 L244 280 H0 Z" fill="var(--orange)"/>
    <rect x="530" y="286" width="519" height="63" fill="url(#addrBar)"/>
    <path d="M0 286 H518 Q536 286 536 317 Q536 349 518 349 H0 Z" fill="url(#callBar)" stroke="#ffffff" stroke-width="3"/>
  </svg>

  <p class="doctor-name">DR. LORVIK TAMSEN , D.D.S</p>

  <p class="tagline">DON’T DRIVE TO THE CITY A COUPLE HOURS AWAY FOR <em>ORAL SURGEON</em></p>
  <h1 class="headline">I’M HERE AT YOUR HOME</h1>

  <div class="brand"><span class="brand__dot"></span>TAMSEN<br>ORAL SURGERY</div>

  <ul class="services">
    <li class="service"><span class="service__photo" role="img" aria-label="Surgeon placing a dental implant" style="background:linear-gradient(135deg,#2b2f36,#c9a08a 55%,#e7e2de)"></span><p class="service__label">Implants</p></li>
    <li class="service"><span class="service__photo" role="img" aria-label="Illustration of a wisdom tooth extraction" style="background:linear-gradient(135deg,#c8353b,#efe6d8 55%,#b9bcc0)"></span><p class="service__label">Wisdom Teeth</p></li>
    <li class="service"><span class="service__photo" role="img" aria-label="Patient being examined for jaw surgery" style="background:linear-gradient(135deg,#6FCCEA,#e3c6b3 50%,#4a55c8)"></span><p class="service__label">Jaw Surgery</p></li>
    <li class="service"><span class="service__photo" role="img" aria-label="Patient receiving facial trauma treatment" style="background:linear-gradient(135deg,#b8aea3,#e2c3ab 50%,#e9e9ea)"></span><p class="service__label">Facial Trauma</p></li>
  </ul>

  <div class="call">
    <span class="call__lead">CALL US</span>
    <span class="call__number">
      <svg width="26" height="30" viewBox="0 0 26 28" aria-hidden="true"><path d="M6 3 L10 3 L12 9 L9 11 Q10 16 13 19 L15 16 L20 18 L20 22 Q18 26 13 24 Q3 18 3 8 Q3 4 6 3 Z" fill="none" stroke="#fff" stroke-width="2.6" stroke-linejoin="round" transform="rotate(-8 12 14)"/><path d="M18 8 Q21 11 18 14 M21 5 Q26 11 21 17" fill="none" stroke="#fff" stroke-width="2" stroke-linecap="round"/></svg>
      (580) 555-0147
    </span>
  </div>

  <p class="address">
    <svg width="16" height="22" viewBox="0 0 16 22" aria-hidden="true"><path d="M8 1 C3.5 1 1 4.5 1 8 C1 13 8 21 8 21 C8 21 15 13 15 8 C15 4.5 12.5 1 8 1 Z" fill="none" stroke="#fff" stroke-width="2"/><circle cx="8" cy="8" r="2.6" fill="#fff"/></svg>
    417 N Harlow Ave. Ada, OK 74820, USA
  </p>
</section>
</body>
</html>
```